Business card with branding treatment

I need to improve the stock logo created with the tool. Also I want a business card with typeface colors matching for modern upscale real estate agency. The clients are looking for upscale agency that is well established and professional. Palm Beach county is an upscale, luxury market. We handle new construction and mostly newer, modern homes. We offer internet marketing for home sellers and take advantage of social media. This logo will be on facebook and instagram channels as well as Youtube videos.

Target Market(s)

Home buyers and sellers nin Plam Beach Florida

Industry/Entity Type

Real Estate

Contact Information for Business Card

Logos name and contact info including youtube and facebook adresses

Font styles to use
Sans Serif

Requirements
Nice to have
• two versions one blue/white the other black/gold or black silver
Should not have
• scripted fonts

```html
<!DOCTYPE html>
<html lang="en">
<head>
<meta charset="UTF-8">
<title>Coastal Crest — Business Card</title>
<link rel="stylesheet" href="https://fonts.googleapis.com/css2?family=Montserrat:wght@300;400&family=Arimo:wght@400&display=swap">
<style>
  :root {
    --page: #1c1c1e;
    --card: #0b0b0c;
    --band: #1f78b9;
    --accent: #29a3e8;
    --accent-deep: #1f78b9;
    --text: #ffffff;
    --rule: #4a4a4a;
  }
  * { box-sizing: border-box; margin: 0; padding: 0; }
  html, body { width: 1200px; height: 900px; overflow: hidden; background: var(--page); }
  .canvas {
    width: 1200px; height: 900px;
    display: flex; align-items: center; justify-content: center; gap: 40px;
  }
  .card {
    position: relative;
    width: 540px; height: 310px;
    background: var(--card);
    border-radius: 22px;
    overflow: hidden;
    box-shadow: 0 18px 40px rgba(0,0,0,.55);
  }
  .card__band {
    position: absolute; left: 0; right: 0; bottom: 0;
    height: 58px; background: var(--band);
  }
  .brand {
    font-family: "Montserrat", sans-serif;
    font-weight: 300;
    color: var(--accent);
    letter-spacing: 1px;
    white-space: nowrap;
  }
  /* front */
  .front__brand-area {
    position: absolute; left: 0; top: 0; width: 250px; height: 252px;
    display: flex; flex-direction: column; align-items: center; justify-content: center; gap: 22px;
  }
  .front__brand { font-size: 25px; }
  .broker {
    font-family: "Montserrat", sans-serif; font-weight: 400;
    font-size: 15px; color: var(--accent-deep); display: flex; align-items: center; gap: 8px;
  }
  .broker__dot { width: 14px; height: 14px; border-radius: 50%; background: var(--accent-deep); }
  .front__divider {
    position: absolute; left: 250px; top: 44px; width: 1px; height: 166px; background: var(--rule);
  }
  .contact {
    position: absolute; left: 276px; top: 50px;
    font-family: "Arimo", sans-serif; color: var(--text);
  }
  .contact__name {
    font-family: "Montserrat", sans-serif; font-weight: 300;
    font-size: 19px; color: var(--accent); letter-spacing: .5px;
  }
  .contact__title { font-size: 13px; margin-bottom: 10px; }
  .contact__list { list-style: none; font-size: 12.5px; line-height: 20px; }
  .contact__list li { display: flex; align-items: center; gap: 7px; }
  .contact__list svg { width: 12px; height: 12px; flex: none; }
  .contact__web-mid { color: var(--accent-deep); }
  .contact__address { font-size: 12.5px; line-height: 17px; margin-top: 10px; padding-left: 19px; }
  .social {
    position: absolute; left: 0; width: 250px; bottom: 0; height: 58px;
    display: flex; align-items: center; justify-content: center; gap: 16px;
    font-family: "Arimo", sans-serif; font-size: 12px; color: var(--text);
  }
  /* back */
  .back__brand-area {
    position: absolute; left: 0; right: 0; top: 0; height: 252px;
    display: flex; align-items: center; justify-content: center;
  }
  .back__brand { font-size: 38px; }
  .badge {
    position: absolute; left: 50%; bottom: 16px; transform: translateX(-50%);
    width: 26px; height: 26px; background: var(--text);
  }
</style>
</head>
<body>
<main class="canvas">
  <section class="card card--front" aria-label="Business card front">
    <div class="front__brand-area">
      <div class="brand front__brand">COASTAL CREST</div>
      <div class="broker"><span class="broker__dot"></span>Meridian Realty Group</div>
    </div>
    <div class="front__divider"></div>
    <div class="contact">
      <div class="contact__name">MARCUS ELLERY</div>
      <div class="contact__title">Managing Director</div>
      <ul class="contact__list">
        <li>
          <svg viewBox="0 0 24 24" aria-hidden="true"><path fill="#29a3e8" d="M6.6 10.8a15 15 0 0 0 6.6 6.6l2.2-2.2a1 1 0 0 1 1-.25 11.4 11.4 0 0 0 3.6.57 1 1 0 0 1 1 1V20a1 1 0 0 1-1 1A17 17 0 0 1 3 4a1 1 0 0 1 1-1h3.5a1 1 0 0 1 1 1c0 1.25.2 2.45.57 3.6a1 1 0 0 1-.25 1z"/></svg>
          044-310 772 518
        </li>
        <li>
          <svg viewBox="0 0 24 24" aria-hidden="true"><rect x="2" y="5" width="20" height="14" fill="#29a3e8"/><path d="M2 5l10 8 10-8" fill="none" stroke="#0b0b0c" stroke-width="2"/></svg>
          info@coastalcrest.com
        </li>
        <li>
          <svg viewBox="0 0 24 24" aria-hidden="true"><g fill="none" stroke="#29a3e8" stroke-width="2"><circle cx="12" cy="12" r="10"/><ellipse cx="12" cy="12" rx="4" ry="10"/><path d="M2 12h20M4 7h16M4 17h16"/></g></svg>
          <span>www.<span class="contact__web-mid">coastalcrestre</span>.com</span>
        </li>
      </ul>
      <p class="contact__address">218, Seaview Avenue Suite 4<br>33480, United States</p>
    </div>
    <div class="card__band"></div>
    <div class="social"><span>/coastalcrest</span><span>@coastalcrest</span></div>
  </section>

  <section class="card card--back" aria-label="Business card back">
    <div class="back__brand-area">
      <div class="brand back__brand">COASTAL CREST</div>
    </div>
    <div class="card__band"></div>
    <div class="badge" aria-label="Membership badge"></div>
  </section>
</main>
</body>
</html>
```